Create a Brochure Design for Brantley Homecare

Brantley Homecare is a subsidiary of the Brantley Care Group. This brochure is specifically for the Brantley Homecare company and brand. Create a 3 panel, A4, front and back, tri-fold brochure. This brochure will be a way to introduce our Homecare services to the community, prospective clients, and various referral partners. The brochure must be eye catching, unique in its deliverables and demonstrate both attention to detail and comfort. Our organization is sophisticated and built around warmth, care and individualized personal attention. The most important aspect of this design is to focus on creating a nurturing, warm, and inviting feel where you would want to have a Nurse or Nurse’s Aide in your own home or a loved one’s home.

I am open to the creativity of the designer to develop something based on the above criteria; however I would like the design to work well with the existing collateral material. What I mean by that is that while I want everything to have its own personality and stand out as its own brand representative, I still need to be able to tell that the overall design concept stays stylistically inside of the same ‘family’ of existing designed material. Because of this, below I would like for the designer to pull inspiration from the link to our website (Located below) as well as from the attachment of our recently refreshed business cards (Attached). This should allow each design to be unique and creative, while still staying inside of a framework and the feel/style that I am looking for.

Finally, I want all the designers to understand that this brochure design is for a private, in home, healthcare company where we are responsible for providing personalized care for a culturally and ethnically diverse make-up clientele of all ages. The photos that are used must represent an image of warmth, care, and a positive interaction between client and caregiver.

Look under the Brantley Homecare tab at www.brantleycaregroup-example.net

Industry/Entity Type

Healthcare

Requirements
Must have
• • The Brantley Homecare company logo must be included.

```html
<!DOCTYPE html>
<html lang="en">
<head>
<meta charset="utf-8">
<title>Brantley Homecare – Services Brochure</title>
<link href="https://fonts.googleapis.com/css2?family=Gentium+Book+Plus:ital,wght@0,400;0,700;1,400&display=swap" rel="stylesheet">
<style>
  :root{
    --backdrop:#55585d;
    --salmon:#f0917a;
    --salmon-deep:#e8775f;
    --salmon-soft:#f7b9a3;
    --cream:#fdf1dc;
    --cream-deep:#fbe4bf;
    --ink:#5b4433;
    --white:#fffaf5;
  }
  *{box-sizing:border-box;margin:0;padding:0}
  html,body{width:1200px;height:800px;overflow:hidden}
  body{background:var(--backdrop);font-family:"Gentium Book Plus",serif;color:var(--ink)}
  .brochure{position:absolute;left:91px;top:40px;width:1018px;height:720px;display:flex;box-shadow:0 10px 30px rgba(0,0,0,.35)}
  .panel{position:relative;width:339.33px;height:720px;overflow:hidden;background:linear-gradient(180deg,var(--cream),var(--cream-deep))}
  .panel + .panel{border-left:1px solid rgba(160,120,80,.15)}
  .panel-art{position:absolute;inset:0;width:100%;height:100%}
  .panel-content{position:absolute;left:30px;right:26px}
  h2{font-weight:400;color:var(--salmon-deep);font-size:24px;line-height:1.15;margin-bottom:8px}
  p{font-size:14px;line-height:1.36}
  .care-list{list-style:none;margin-top:10px;margin-left:20px}
  .care-list li{font-size:14px;line-height:1.36;position:relative;padding-left:18px}
  .care-list li::before{content:"";position:absolute;left:0;top:6px;width:9px;height:9px;border-radius:50%;background:var(--salmon)}
  .section + .section{margin-top:20px}
  .quote{position:absolute;left:40px;top:132px;width:160px;color:var(--white);font-size:13px;line-height:1.35;font-style:italic}
  .quote-mark{position:absolute;color:var(--white);font-size:58px;line-height:1;font-family:"Gentium Book Plus",serif}
  .quote-open{left:14px;top:124px}
  .quote-close{left:150px;top:178px}
  .on-salmon, .on-salmon h2{color:var(--white)}
  .on-salmon h2{font-size:28px}
  .on-salmon p{font-size:13px;line-height:1.38}
  .on-salmon p + p{margin-top:9px}
</style>
</head>
<body>
<main class="brochure">

  <section class="panel panel-services">
    <svg class="panel-art" viewBox="0 0 339 720" preserveAspectRatio="none">
      <defs>
        <linearGradient id="gardenTone" x1="0" y1="0" x2="1" y2="1">
          <stop offset="0" stop-color="#6f8f4a"/>
          <stop offset=".5" stop-color="#9aa870"/>
          <stop offset="1" stop-color="#8a7a5c"/>
        </linearGradient>
      </defs>
      <path d="M0 255 Q170 290 339 245 V280 Q170 320 0 285 Z" fill="var(--cream-deep)" opacity=".7"/>
      <path role="img" aria-label="Photo: a caregiver walking in a garden with an elderly client using a walker" d="M0 0 H339 V245 Q170 285 0 255 Z" fill="url(#gardenTone)"/>
    </svg>
    <div class="panel-content" style="top:292px">
      <div class="section">
        <h2>Home Assistants</h2>
        <p>Will provide companionship, assist with meal preparation, and light housekeeping (dusting, vacuuming, mopping, sweeping, bathroom and kitchen clean up, linen change and laundry). Sorry, no heavy cleaning. No hands-on assistance.</p>
      </div>
      <div class="section">
        <h2>Nurses Aide / Assistants</h2>
        <p>Help with all services as Home Assistants but they'll also help with personal care:</p>
        <ul class="care-list">
          <li>Bathing</li>
          <li>Toileting</li>
          <li>Incontinent care</li>
          <li>Dressing</li>
          <li>Transferring the client from bed, bath or car</li>
          <li>Range of motion exercises</li>
          <li>Turning and positioning</li>
          <li>Assistance with a wheelchair or walker</li>
        </ul>
      </div>
    </div>
  </section>

  <section class="panel panel-nursing">
    <svg class="panel-art" viewBox="0 0 339 720" preserveAspectRatio="none">
      <defs>
        <linearGradient id="handsTone" x1="0" y1="0" x2="1" y2="1">
          <stop offset="0" stop-color="#fbf3ee"/>
          <stop offset=".5" stop-color="#e2b49a"/>
          <stop offset="1" stop-color="#f6ebe4"/>
        </linearGradient>
      </defs>
      <path d="M0 0 H339 V215 Q200 280 0 265 Z" fill="var(--salmon)"/>
      <path d="M0 265 Q200 280 339 215 V240 Q200 300 0 285 Z" fill="var(--salmon-soft)" opacity=".6"/>
      <rect role="img" aria-label="Photo: a caregiver's hands holding an elderly person's hands" x="22" y="18" width="140" height="96" fill="url(#handsTone)"/>
    </svg>
    <span class="quote-mark quote-open">“</span>
    <p class="quote">The capacity to care is the thing which gives life its deepest significance.</p>
    <span class="quote-mark quote-close">”</span>
    <div class="panel-content" style="top:300px">
      <p>(This level of care is appropriate for patients with Alzheimer's and Dementia) Sorry, no heavy cleaning.</p>
      <div class="section" style="margin-top:22px">
        <h2>Skilled Nurses</h2>
        <p>We offer a wide range of skilled nursing services ranging from Licensed Practical Nurses (LPN) to Registered Nurses (RN).</p>
      </div>
      <div class="section">
        <h2>Transportation Services / Escort &amp; Errand Services</h2>
        <p>If a Brantley Homecare client who already is receiving personal care services requests that our caregiver provide escort or errand services, such as grocery shopping, errands or outings, there will be an additional fee assessed to the client.</p>
      </div>
    </div>
  </section>

  <section class="panel panel-about">
    <svg class="panel-art" viewBox="0 0 339 720" preserveAspectRatio="none">
      <defs>
        <linearGradient id="vanTone" x1="0" y1="0" x2="1" y2="1">
          <stop offset="0" stop-color="#9a9c9e"/>
          <stop offset=".5" stop-color="#5e6164"/>
          <stop offset="1" stop-color="#b5b0a6"/>
        </linearGradient>
      </defs>
      <rect width="339" height="720" fill="var(--salmon)"/>
      <path d="M0 330 Q170 280 339 290 V315 Q170 310 0 355 Z" fill="var(--cream-deep)"/>
      <path role="img" aria-label="Photo: a caregiver helping a client in a wheelchair onto a van lift" d="M0 355 Q170 310 339 315 V490 Q170 500 0 545 Z" fill="url(#vanTone)"/>
    </svg>
    <div class="panel-content on-salmon" style="top:32px">
      <h2>More than a job...</h2>
      <p>This is more than a job for us. Some people devote their lives to teaching, some to science. For us, it's caring for you or your family member. Our job is simply to make your job easier.</p>
      <p>The Brantley Way is special; it is compassionate, professional, dependable, flexible and is built on the strongest foundation. Everything we do is focused on meeting the individual needs of our clients.</p>
    </div>
    <div class="panel-content on-salmon" style="top:568px">
      <p>Clients who prefer not to pay for these additional charges may choose to take alternate transportation means, such as using their own vehicle (with the caregiver driving) or using public and / or private transportation, such as the CareRide Van.</p>
    </div>
  </section>

</main>
</body>
</html>
```